Business Card Design Project

We need a business card for our new business based in Vancouver called
"Sollu⁵ Calm Spa" We are looking for a simple yet bold design for our business cards that will enable us to stand out from the pack. All business card details will be provided in the handover stage.
Updates

Thank you to all who have submitted

The work is great for the most part
Cards with creative use of the logo
have been more successful so far

Dark cards and rounded edges 
are also getting good reviews

Double sided is an option we would like to see explored

Thank you

Target Market(s)

Our clients are stressed business people, yoga/meditation enthusiast, and people looking for a new experience in a Spa enviroment

Industry/Entity Type

Business

Font styles to use
Other font styles liked:
• please check design file

Requirements
Must have
• Sollu⁵ Calm Spa

2417 E Fenwick Row, Vancouver, BC V5K 3H9

sollu@calmspa-example.ca
Nice to have
• Creative approach to layout and design

Outside of the box design elements
Should not have
• Should not be too busy

```html
<!DOCTYPE html>
<html lang="en">
<head>
<meta charset="utf-8">
<title>Sollu⁵ Calm Spa — Business Card</title>
<link rel="stylesheet" href="https://fonts.googleapis.com/css2?family=Questrial&display=swap">
<style>
  :root {
    --page-bg: #f6f4f0;
    --card-black: #151419;
    --card-silver: #e4e5ea;
    --card-grey: #5c5c66;
    --text-grey: #8b8b93;
    --brand-blue: #4d54a0;
  }
  * { margin: 0; padding: 0; box-sizing: border-box; }
  html, body {
    width: 1200px;
    height: 849px;
    overflow: hidden;
    background: var(--page-bg);
    font-family: "Questrial", Arial, sans-serif;
  }
  .card {
    position: absolute;
    left: 275px;
    top: 228px;
    width: 650px;
    height: 392px;
    border-radius: 38px 72px 72px 38px;
    background: linear-gradient(90deg,
      var(--card-silver) 0%,
      #b9bac2 9%,
      var(--card-grey) 20%,
      #26252c 31%,
      var(--card-black) 40%,
      var(--card-black) 100%);
    color: var(--text-grey);
    overflow: hidden;
  }
  .brand {
    position: absolute;
    left: 48px;
    top: 350px;
    transform: rotate(-90deg);
    transform-origin: left top;
    display: flex;
    align-items: center;
    gap: 12px;
    white-space: nowrap;
    height: 40px;
  }
  .brand-name {
    font-size: 28px;
    line-height: 40px;
    letter-spacing: 1px;
    color: var(--brand-blue);
  }
  .brand-dot {
    width: 12px;
    height: 12px;
    border-radius: 50%;
    background: var(--brand-blue);
  }
  .details {
    position: absolute;
    right: 46px;
    text-align: right;
    white-space: nowrap;
  }
  .person { top: 60px; }
  .person-name { font-size: 21px; letter-spacing: 3px; }
  .person-role { font-size: 13px; letter-spacing: 2px; margin-top: 2px; }
  .contact { top: 182px; }
  .contact-phone { font-size: 21px; letter-spacing: 3px; }
  .contact-email { font-size: 17px; letter-spacing: 2.2px; margin-top: 8px; }
  .company { top: 322px; }
  .company-address,
  .company-email { font-size: 12px; letter-spacing: 1.8px; line-height: 20px; }
</style>
</head>
<body>
  <div class="card">
    <div class="brand">
      <span class="brand-dot"></span>
      <span class="brand-name">Sollu⁵ Calm Spa</span>
    </div>

    <div class="details person">
      <p class="person-name">Corwin Aldous Fenmarrow</p>
      <p class="person-role">Health Consultant</p>
    </div>

    <div class="details contact">
      <p class="contact-phone">+098 555 017342</p>
      <p class="contact-email">cf_sollu@calmspa-example.ca</p>
    </div>

    <div class="details company">
      <p class="company-address">2417 E Fenwick Row, Vancouver, BC V5K 3H9</p>
      <p class="company-email">sollu@calmspa-example.ca</p>
    </div>
  </div>
</body>
</html>
```